Australian Raw Honey Label Design for Floravine Honey

We need a new label design for our honey jars. Previous label was very amateurish and we need a new more professional look. We are also changing name to Floravine; which means kiss in French. The label should be simple, fluid, with simple drawings of flowers, bees in the décor reflecting the minimal process we use in producing our honey.
I would like to use my profile (curly/afro hair) (that people can recognise ) that connects with bees. The colour scheme should be warm sun, yellow or orange without too many colours or heavy background.

Label size: 200 mm x 60 mm
there are two variantes of the label, one with 1kg and the other with 500g
More information in the attached brief.

Target Market(s)

customer looking for locally produced honey vs commercial supermarket honey. Product sold mostly through word of mouth

Colors
ffc214
f78f20
f68e4e
fbed22

Requirements
Must have
• Included in the brief as per food label requirement
Nice to have
• curve, flowy font for brand name
• Brand means kiss, so connection with bees is important.
Should not have
• heavy background colors

```html
<!DOCTYPE html>
<html lang="en">
<head>
<meta charset="utf-8">
<title>Floravine Honey – Jar Label 500g</title>
<link href="https://fonts.googleapis.com/css2?family=Amatic+SC:wght@400;700&family=Roboto:wght@300;400&display=swap" rel="stylesheet">
<style>
  :root{
    --label-yellow:#fdc21a;
    --sun-glow:#fbed22;
    --honey-orange:#f7a620;
    --ink-brown:#7b4a22;
    --brand-brown:#8a5226;
    --badge-green:#1f8a3c;
    --badge-white:#ffffff;
  }
  *{box-sizing:border-box;margin:0;padding:0}
  html,body{width:1200px;height:385px;overflow:hidden;background:var(--label-yellow)}
  .label{position:relative;width:1200px;height:385px;background:var(--label-yellow);
    font-family:"Roboto",Arial,sans-serif;color:var(--ink-brown);}

  /* brand block */
  .brand{position:absolute;left:58px;top:22px;width:290px;text-align:center;color:var(--brand-brown);font-family:"Amatic SC",cursive}
  .brand-name{font-size:46px;font-weight:700;line-height:1;letter-spacing:1px}
  .brand-tagline{font-size:31px;font-weight:400;line-height:1.1;margin-top:4px;letter-spacing:.5px}
  .portrait-art{position:absolute;left:72px;top:108px;width:262px;height:238px;border-radius:50%;
    background:radial-gradient(circle at 50% 50%,var(--sun-glow) 0%,#fde13a 45%,var(--label-yellow) 72%)}

  .weight-rule{position:absolute;left:0;right:0;top:349px;height:1px;background:var(--ink-brown)}
  .net-weight{position:absolute;left:160px;top:336px;padding:0 8px;background:var(--label-yellow);
    font-size:22px;font-weight:300;color:var(--ink-brown);line-height:26px}

  /* info columns */
  .info-col{position:absolute}
  .col-left{left:366px;top:33px;width:275px}
  .col-right{left:874px;top:33px;width:296px}
  .info-item{position:relative;padding-left:24px}
  .bullet{position:absolute;left:0;top:2px;width:17px;height:17px;border-radius:50%;
    background:var(--honey-orange);border:2px solid var(--ink-brown)}
  .info-title{font-size:15.5px;font-weight:400;line-height:19px}
  .info-value{font-size:15.5px;font-weight:400;line-height:19px}
  .gap-md{margin-top:24px}
  .about{font-size:15.5px;font-weight:300;line-height:19.3px;text-align:justify;hyphens:auto;margin-top:14px}
  .storage-text{font-size:15.5px;font-weight:300;line-height:19.3px;text-align:justify;hyphens:auto;margin-left:-24px}
  .storage-lead{font-weight:400;margin-left:0}

  .bee-art{position:absolute;left:1122px;top:32px;width:46px;height:30px;border-radius:50%;
    background:radial-gradient(circle,#6b4a1e 0%,#b88a2a 55%,transparent 75%)}
  .origin-badge{position:absolute;left:1118px;top:262px;width:51px;height:75px;border-radius:4px;
    background:var(--badge-white);border:1px solid #c9b27a;padding:5px}
  .origin-badge span{display:block;width:100%;height:38px;background:var(--badge-green);border-radius:2px}

  /* nutrition panel */
  .nutrition{position:absolute;left:655px;top:30px;width:208px;height:292px;border:1.5px solid var(--ink-brown);
    font-size:10px;font-weight:300;color:var(--ink-brown)}
  .nutrition-title{font-size:14.5px;font-weight:300;text-align:center;padding-top:8px;height:27px}
  .nutrition-line{padding:0 5px;height:22px;line-height:22px;border-bottom:1px solid var(--ink-brown)}
  .nutrition-head{display:grid;grid-template-columns:78px 65px 65px;height:72px;border-bottom:1px solid var(--ink-brown);align-items:center}
  .dipper-art{width:50px;height:56px;margin-left:14px;border-radius:8px;
    background:linear-gradient(160deg,var(--label-yellow) 0%,#e6a21c 60%,#c07a1c 100%)}
  .col-head{font-size:10px;line-height:12px;text-align:center}
  .nutrient-row{display:grid;grid-template-columns:78px 65px 65px;height:21.5px;line-height:21.5px}
  .nutrient-row span:first-child{padding-left:5px}
  .nutrient-row span:not(:first-child){text-align:center}
</style>
</head>
<body>
<div class="label">

  <div class="brand">
    <div class="brand-name">Floravine</div>
    <div class="brand-tagline">Premium raw honey</div>
  </div>
  <div class="portrait-art" role="img" aria-label="Illustration: profile with curly hair formed by a swarm of bees, set on a glowing sun circle"></div>

  <div class="weight-rule"></div>
  <div class="net-weight">500g</div>

  <div class="info-col col-left">
    <div class="info-item">
      <span class="bullet"></span>
      <p class="info-title">Ingredient list:</p>
      <p class="info-value">100% pure Australian Honey</p>
    </div>
    <div class="info-item gap-md">
      <span class="bullet"></span>
      <p class="info-title">Contact us:</p>
      <p class="info-value">e-mail address and phone number</p>
    </div>
    <div class="info-item" style="margin-top:16px">
      <span class="bullet"></span>
      <p class="about" style="margin-top:0;text-indent:0">Floravine (meaning kiss in French) is raw, natural honey made with love by our happy bees. They are foraging on a rich mixed suburban flora in Wattlebrook. Unlike commercial honey which is often pasteurised, our raw honey is not heated which helps preserve the flavour and natural benefits of locally produced honey.</p>
    </div>
  </div>

  <div class="nutrition">
    <div class="nutrition-title">Nutritional information</div>
    <div class="nutrition-line">Servings per package: 25</div>
    <div class="nutrition-line">Serving size: 20g</div>
    <div class="nutrition-head">
      <div class="dipper-art" role="img" aria-label="Illustration: honey dipper dripping honey"></div>
      <div class="col-head">Average Quantity per Serving</div>
      <div class="col-head">Average Quantity per 100 g</div>
    </div>
    <div class="nutrient-row"><span>Energy</span><span>280 kJ</span><span>1400 kJ</span></div>
    <div class="nutrient-row"><span>Protein</span><span>0.0 g</span><span>0.2 g</span></div>
    <div class="nutrient-row"><span>Fat, total</span><span>0.0 g</span><span>0.0 g</span></div>
    <div class="nutrient-row"><span>-saturated</span><span>0.0 g</span><span>0.0 g</span></div>
    <div class="nutrient-row"><span>Carbohydrate</span><span>16.4 g</span><span>82.1 g</span></div>
    <div class="nutrient-row"><span>-sugars</span><span>16.4 g</span><span>82.1 g</span></div>
    <div class="nutrient-row"><span>Sodium</span><span>3 mg</span><span>14 mg</span></div>
  </div>

  <div class="info-col col-right">
    <div class="info-item">
      <span class="bullet"></span>
      <p class="info-title">Storage Instructions:</p>
      <p class="info-value">Store in a cool and dry place.</p>
      <p class="storage-text" style="margin-left:0">Crystallisation is a normal process that happens overtime. This does not alter the quality of the honey however, the process can be reversed by placing the container in hot water (but not more than 45°C) and let it stand until completely liquefied.</p>
    </div>
    <div class="info-item" style="margin-top:16px">
      <span class="bullet"></span>
      <p class="info-title">Batch code:</p>
    </div>
    <div class="info-item" style="margin-top:32px">
      <span class="bullet"></span>
      <p class="info-title">Best before:</p>
    </div>
  </div>

  <div class="bee-art" role="img" aria-label="Illustration: small flying bee"></div>
  <div class="origin-badge" role="img" aria-label="Country of origin badge"><span></span></div>

</div>
</body>
</html>
```